Motivational Quotes Poster Series

This is a 3 poster design series for Ridgeway Haul Academy. The size of each poster should be 18 inches wide and 24 inches tall. The goal of these posters is to serve as motivational "signs" to be hung in the office area for the employees (not customers). These employees are instructors/teachers, teaching students how to drive semi trucks. While each design is a separate poster and design, we're posting as 1 project because we'd like some continuity between the series. Below we'll break down the details of all 3 posters...

Poster #1
Text that must appear on poster - "If You Want The Best Out Of Each Student" and "Give The Best Of You!" Note: While this text must appear on the poster, you can arrange in the layout as you see fit. For example, first line could be at top of poster and second line on bottom.

Poster #2
Text that must appear on poster - "Invest In People" and "Change Someone's Life" (same notes apply as in 1st poster)

Poster #3
Text that must appear on poster - "Today Is..." and "Just Another Day For You" and "The Most Important Day In Their Life" Note: This can be laid out on the poster however you see fit, but each phrase needs to be separate and it needs to flow.

Target Market(s)

Truck Driver Training Instructors - These are middle-aged, mostly male, masculine type personalities.

Industry/Entity Type

Training

Requirements
Must have
• Must have noted text from description
Must have working files (ie - PSD, EPS, AI, etc) provided
Must have common theme between each poster in series
Must have easy to read font and layout
Must have product dimensions of 18 inches (width) by 24 inches (height). If design uses full dimensions please include quarter inch bleed.
Nice to have
• Nice to have a trucking theme...related to trucking industry, but not over the top. Example - This could mean subtle injection of background tire tracks, but by no means are tire tracks required.

For inspiration, you can visit the site at http://www.ridgewayhaulacademy.com. While you can use the colors of the site/logo, you can still branch out between each poster to try new colors within reason.

Note: While we've attached the logo to this project, it COULD be used but doesn't HAVE to be included in the design. The logo IS NOT a focal point. The phrases in the poster ARE the focal point.

```html
<!DOCTYPE html>
<html lang="en">
<head>
<meta charset="utf-8">
<title>If You Want the Best Out of Each Student – Ridgeway Haul Academy</title>
<link rel="stylesheet" href="https://fonts.googleapis.com/css2?family=Tinos:wght@700&display=swap">
<style>
  :root {
    --paper: #ffffff;
    --band-top: #d9d9d9;
    --ink: #111111;
    --green: #3d9a2b;
    --red: #d4241c;
    --curve: #b3261e;
    --stripe: #a9d3ec;
    --stripe-light: #d6ebf7;
    --truck-tone: #c9ccd3;
  }
  html, body {
    margin: 0;
    padding: 0;
    overflow: hidden;
    background: var(--paper);
  }
  .poster {
    position: relative;
    width: 900px;
    height: 1200px;
    overflow: hidden;
    background: var(--paper);
    font-family: "Tinos", "Times New Roman", serif;
    font-weight: 700;
    text-transform: uppercase;
  }
  .top-band {
    position: absolute;
    left: 0; top: 0;
    width: 900px; height: 110px;
    background: linear-gradient(to bottom, var(--band-top), var(--paper));
  }
  .headline {
    position: absolute;
    margin: 0;
    line-height: 1;
    white-space: nowrap;
  }
  .lead {
    right: 30px; top: 108px;
    font-size: 64px;
    color: var(--ink);
    letter-spacing: 1px;
  }
  .lead-sub {
    left: 105px; top: 200px;
    font-size: 33px;
    color: var(--green);
  }
  .give {
    left: 484px; top: 580px;
    font-size: 128px;
    color: var(--ink);
  }
  .give-sub {
    left: 170px; top: 718px;
    font-size: 80px;
    color: var(--red);
  }
  .flow-curve {
    position: absolute;
    left: 0; top: 0;
    width: 900px; height: 1200px;
    pointer-events: none;
  }
  .brand {
    position: absolute;
    right: 36px; top: 988px;
    display: flex;
    align-items: center;
    gap: 8px;
    font-size: 18px;
    color: var(--ink);
    text-transform: none;
  }
  .brand-mark {
    width: 14px; height: 14px;
    background: var(--ink);
  }
  .footer-stripes {
    position: absolute;
    left: 0; top: 1040px;
    width: 820px; height: 40px;
  }
  .truck {
    position: absolute;
    left: 0; top: 1005px;
    width: 140px; height: 82px;
    background: linear-gradient(to right, var(--truck-tone), #eef0f3);
  }
</style>
</head>
<body>
<main class="poster">
  <div class="top-band"></div>

  <h1 class="headline lead">If You Want</h1>
  <p class="headline lead-sub">The Best Out of Each Student</p>

  <svg class="flow-curve" viewBox="0 0 900 1200" aria-hidden="true">
    <path d="M800 232 C 860 290, 520 300, 330 360 C 150 420, 170 520, 300 560 C 370 580, 420 585, 470 590"
          fill="none" stroke="var(--curve)" stroke-width="2.5"/>
  </svg>

  <p class="headline give">Give</p>
  <p class="headline give-sub">The Best of You</p>

  <div class="brand"><span class="brand-mark"></span>Ridgeway Haul Academy</div>

  <svg class="footer-stripes" viewBox="0 0 820 40" aria-hidden="true">
    <rect x="150" y="0" width="40" height="40" fill="var(--stripe-light)"/>
    <rect x="205" y="0" width="36" height="40" fill="var(--stripe)"/>
    <rect x="256" y="0" width="30" height="40" fill="var(--stripe)"/>
    <rect x="300" y="0" width="26" height="40" fill="var(--stripe)"/>
    <rect x="340" y="0" width="24" height="40" fill="var(--stripe)"/>
    <rect x="378" y="0" width="22" height="40" fill="var(--stripe)"/>
    <rect x="414" y="0" width="20" height="40" fill="var(--stripe)"/>
    <rect x="448" y="0" width="18" height="40" fill="var(--stripe)"/>
    <rect x="480" y="0" width="16" height="40" fill="var(--stripe)"/>
    <rect x="510" y="0" width="14" height="40" fill="var(--stripe)"/>
    <rect x="538" y="0" width="12" height="40" fill="var(--stripe)"/>
    <rect x="564" y="0" width="10" height="40" fill="var(--stripe)"/>
    <rect x="588" y="0" width="9" height="40" fill="var(--stripe-light)"/>
    <rect x="611" y="0" width="8" height="40" fill="var(--stripe-light)"/>
    <rect x="633" y="0" width="7" height="40" fill="var(--stripe-light)"/>
    <rect x="654" y="0" width="6" height="40" fill="var(--stripe-light)"/>
    <rect x="674" y="0" width="5" height="40" fill="var(--stripe-light)"/>
  </svg>

  <div class="truck" role="img" aria-label="Semi truck with white trailer driving to the left"></div>
</main>
</body>
</html>
```